Website for our 3rd party logistics warehouse company

Our company is a 3rd party logistics company. We receive and ship other businesses products for them. We offer our services to other smaller businesses that do not have a warehouse to operate out of. We also help many Brindlemart businesses prepare their products to be sold on Brindlemart.

We are looking for a modern looking design for our website. Please see our attached logo for design ideas. We are open to changing logo colors for website.

We really like the look of the website www.quorvane.com

Target Market(s)

Other businesses and brands of products

Industry/Entity Type

Warehousing and shipping

Number of Pages Required

2 page

Requirements
Must have
• We need 2 pages. Our main landing page and a duplicate page with different information geared towards brands.
Nice to have
• I like the look of overlay/transparent sections. Please see quorvane.com there is a ribbon that shows "Partners".

```html
<!DOCTYPE html>
<html lang="en">
<head>
<meta charset="utf-8">
<title>Halcyon 3PL — Prep &amp; Fulfilment</title>
<link href="https://fonts.googleapis.com/css2?family=Poppins:wght@400;500;600;700&display=swap" rel="stylesheet">
<style>
  :root{
    --white:#ffffff;
    --page-bg:#ffffff;
    --header:#2b2a35;
    --hero-a:#4a4650;
    --hero-b:#6b5a4c;
    --band:#10587a;
    --brand-blue:#179bd7;
    --benefit-a:#1b1c22;
    --benefit-b:#34302e;
    --contact-a:#23451f;
    --contact-b:#3d6a34;
    --footer:#8a8a94;
    --accent:#fbbf35;
    --accent-logo:#f2c230;
  }
  *{margin:0;padding:0;box-sizing:border-box}
  html,body{width:1200px;height:2401px;overflow:hidden;background:var(--page-bg)}
  body{font-family:"Poppins",sans-serif;color:var(--white)}
  .page{position:absolute;left:0;top:0;width:1288px;height:2576px;transform:scale(0.93168);transform-origin:0 0}
  .abs{position:absolute}

  .hero-photo{left:70px;top:64px;width:1148px;height:568px;background:linear-gradient(115deg,var(--hero-a) 0%,#55505a 40%,var(--hero-b) 100%)}
  .site-header{left:70px;top:64px;width:1148px;height:86px;background:var(--header);opacity:.92}
  .logo{left:138px;top:94px;font-size:13px;font-weight:600;letter-spacing:1px;color:var(--white)}
  .menu{left:1122px;top:97px}
  .hero-shade{left:70px;top:586px;width:1148px;height:46px;background:rgba(40,38,45,.6)}
  .quote-open{left:135px;top:255px}
  .quote-close{left:702px;top:450px}
  .hero-title{left:130px;top:284px;font-size:38px;font-weight:600;letter-spacing:1px}
  .hero-text{left:130px;top:336px;width:680px;font-size:17.5px;font-weight:500;line-height:43px}

  .band{left:70px;top:632px;width:1148px;height:42px;background:var(--band)}
  .why{left:70px;top:674px;width:1148px;height:432px;background:var(--brand-blue)}
  .why-title{left:136px;top:698px;font-size:33px;font-weight:600;letter-spacing:1px}
  .why-item{width:290px;text-align:center;font-size:19px;font-weight:500;line-height:25px}
  .why-icon{display:block;margin:0 auto 6px}
  .why-divider{width:2px;height:40px;background:var(--white);top:868px}

  .benefits-photo{left:70px;top:1106px;width:1148px;height:451px;background:linear-gradient(120deg,var(--benefit-a),#2a2a30 55%,var(--benefit-b))}
  .benefits-title{left:130px;top:1132px;font-size:60px;font-weight:600;letter-spacing:7px;line-height:1}
  .benefits-rule{left:311px;top:1207px;width:105px;height:11px;background:var(--white)}
  .benefit-list{left:130px;top:1238px;list-style:none;font-size:18.5px;font-weight:500}
  .benefit-list li{height:61px;padding-left:22px;position:relative}
  .benefit-list li::before{content:"";position:absolute;left:1px;top:13px;width:8px;height:8px;border-radius:50%;background:var(--white)}

  .promise{left:70px;top:1557px;width:1148px;height:316px;background:var(--brand-blue)}
  .promise-col{text-align:center;font-size:15.5px;font-weight:500;line-height:20px}
  .promise-col h2{font-size:28px;font-weight:500;margin-bottom:26px;line-height:1.3}
  .promise-divider{left:612px;top:1595px;width:2px;height:173px;background:var(--white)}

  .contact-photo{left:70px;top:1873px;width:1148px;height:564px;background:radial-gradient(ellipse at 55% 45%,var(--contact-b),var(--contact-a) 75%)}
  .contact-title{left:70px;width:1086px;top:1900px;text-align:center;font-size:48px;font-weight:600;letter-spacing:1px}
  .field-label{left:409px;font-size:19px;font-weight:500}
  .field{left:409px;width:470px;background:var(--white);border:none;border-radius:6px}
  .field-area{border-radius:12px}
  .send-btn{left:539px;top:2357px;width:210px;height:44px;background:var(--accent);color:var(--white);border:none;font-family:"Poppins",sans-serif;font-size:18px;font-weight:500;border-radius:2px}

  .site-footer{left:70px;top:2437px;width:1148px;height:75px;background:var(--footer)}
  .fine-print{left:128px;top:2447px;width:310px;font-size:4.6px;line-height:7px;color:var(--white)}
</style>
</head>
<body>
<div class="page">

  <div class="abs hero-photo" role="img" aria-label="Hands holding a tablet over printed sales charts on a wooden desk"></div>
  <header class="abs site-header"></header>
  <div class="abs logo">HALCYON 3PL</div>
  <svg class="abs menu" width="36" height="22" viewBox="0 0 36 22"><rect y="0" width="36" height="4" fill="#fff"/><rect y="9" width="36" height="4" fill="#fff"/><rect y="18" width="36" height="4" fill="#fff"/></svg>
  <div class="abs hero-shade"></div>

  <svg class="abs quote-open" width="68" height="28" viewBox="0 0 68 28" fill="#fff"><path d="M0 0h28v14L12 28v-12H0z"/><path d="M38 0h28v14L50 28v-12H38z"/></svg>
  <h1 class="abs hero-title">WHO WE ARE</h1>
  <p class="abs hero-text">Halcyon 3PL is your one stop 3PL that will help you grow your business and allow you to be hands off. We offer high end services and meet our commitment, guaranteed.</p>
  <svg class="abs quote-close" width="68" height="28" viewBox="0 0 68 28" fill="#fff"><path d="M0 0h28v12L12 28v-14H0z"/><path d="M38 0h28v12L50 28v-14H38z"/></svg>

  <div class="abs band"></div>
  <section class="abs why"></section>
  <h2 class="abs why-title">WHY USE A PREP 3PL</h2>

  <div class="abs why-item" style="left:92px;top:802px">
    <svg class="why-icon" width="66" height="66" viewBox="0 0 66 66"><circle cx="33" cy="33" r="30" fill="none" stroke="#fff" stroke-width="4"/><rect x="18" y="24" width="30" height="20" rx="3" fill="#fff"/><rect x="27" y="19" width="12" height="6" rx="2" fill="none" stroke="#fff" stroke-width="3"/><rect x="18" y="32" width="30" height="2" fill="#179bd7"/></svg>
    Work from anywhere<br>in the world.
  </div>
  <div class="abs why-divider" style="left:361px"></div>
  <div class="abs why-item" style="left:349px;top:802px">
    <svg class="why-icon" width="66" height="66" viewBox="0 0 66 66"><circle cx="33" cy="33" r="30" fill="none" stroke="#fff" stroke-width="4"/><g stroke="#fff" stroke-width="3" fill="none" stroke-linecap="round"><path d="M17 22l3 3 5-5M17 33l3 3 5-5M17 44l3 3 5-5"/><path d="M30 23h18M30 34h18M30 45h18"/></g></svg>
    Don't have to manage employees, health insurance plans, payroll, sick calls, etc.
  </div>
  <div class="abs why-divider" style="left:632px"></div>
  <div class="abs why-item" style="left:640px;top:802px">
    <svg class="why-icon" width="66" height="66" viewBox="0 0 66 66"><circle cx="33" cy="33" r="30" fill="none" stroke="#fff" stroke-width="4"/><path d="M25 29v-7a8 8 0 0 1 16 0" fill="none" stroke="#fff" stroke-width="4"/><rect x="21" y="29" width="24" height="19" rx="3" fill="#fff"/><circle cx="33" cy="37" r="3" fill="#179bd7"/><rect x="32" y="38" width="2" height="6" fill="#179bd7"/></svg>
    Don't get locked into<br>a 3-5 year warehouse lease where you guarantee hundreds of thousands of dollars
  </div>
  <div class="abs why-divider" style="left:936px"></div>
  <div class="abs why-item" style="left:906px;top:802px">
    <svg class="why-icon" width="66" height="66" viewBox="0 0 66 66"><circle cx="33" cy="33" r="30" fill="none" stroke="#fff" stroke-width="4"/><rect x="28" y="19" width="22" height="16" rx="2" fill="none" stroke="#fff" stroke-width="3"/><path d="M32 31l5-5 3 3 6-6" fill="none" stroke="#fff" stroke-width="2.5"/><circle cx="22" cy="33" r="5" fill="#fff"/><path d="M13 47a9 9 0 0 1 18 0z" fill="#fff"/></svg>
    Grow your business<br>without commitment
  </div>

  <div class="abs benefits-photo" role="img" aria-label="Laptop screen showing a sales dashboard in a dim office"></div>
  <h2 class="abs benefits-title">BENEFITS:</h2>
  <div class="abs benefits-rule"></div>
  <ul class="abs benefit-list">
    <li>48 hour turn around guarantee – done in 48 hours or its free*</li>
    <li>No monthly subscription – only pay for what you use</li>
    <li>No receiving fees</li>
    <li>No pallet or outbound fees</li>
    <li>Email and phone support</li>
  </ul>

  <section class="abs promise"></section>
  <div class="abs promise-col" style="left:120px;top:1603px;width:468px">
    <h2>Our software</h2>
    Know what inventory is at our warehouse in real time.<br>Our software allows you to track your inventory<br>and know how your shipment status in real time. Professional<br>software designed specifically for our needs.
  </div>
  <div class="abs promise-divider"></div>
  <div class="abs promise-col" style="left:640px;top:1602px;width:528px">
    <h2>Our Guarantee</h2>
    All orders will be prepped and ready for shipment<br>in 48 business hours (often 24 or less) and we guarantee it.<br>We are confident in our services and<br>if we do not fulfill our obligation, we offer a 500 item (up to $700)<br>credit on your next shipment.
  </div>

  <div class="abs contact-photo" role="img" aria-label="Wooden letter tiles spelling contact on green felt"></div>
  <h2 class="abs contact-title">CONTACT US</h2>
  <label class="abs field-label" style="top:2013px">Name</label>
  <div class="abs field" style="top:2044px;height:43px"></div>
  <label class="abs field-label" style="top:2099px">Email</label>
  <div class="abs field" style="top:2128px;height:43px"></div>
  <label class="abs field-label" style="top:2183px">Messages</label>
  <div class="abs field field-area" style="top:2212px;height:123px"></div>
  <button class="abs send-btn">Send Message</button>

  <footer class="abs site-footer"></footer>
  <p class="abs fine-print">*Our guarantee is 48 hours from the time an outbound shipment is created in our system. Weekends and holidays excluded. Orders created on a Friday after hours or on a weekend count from Monday morning. We offer a credit of up to 500 units on your next shipment. Credits cover standard prep items only. We cannot control shipping companies and freight carriers.</p>

</div>
</body>
</html>
```